Ridgeway Moss - Facebook Cover Photo & Photo Icon Design

We’re looking for a Facebook Cover Photo and Profile Icon design for Ridgeway Moss, a leading Residential Real Estate brand under Ridgeway Property Agents, based in Capalaba and Alexandra Hills, Queensland, Australia.

This design will represent my professional real estate profile and needs to be bold, clean, and on-brand.

Deliverables:

Facebook Cover Photo (820 x 312 px, optimized for mobile + desktop)

Facebook Profile Icon (1:1 ratio, minimum 320 x 320 px)

Design Guidelines:

1. Must Include:

The Ridgeway Moss logo (provided after project start)

Use of the Ridgeway Property Agents brand colour palette (will be supplied)

Clear connection to residential real estate

2. Optional but Preferred:

A local photo or skyline of Capalaba or Alexandra Hills in QLD (bonus points for this)

Space for a short tagline like:
“Selling Faster. Selling Smarter. Selling Ridgeway.”
(Optional tagline – open to variations if it improves layout/design)

3. Style & Feel:

Professional yet personable

Clean, modern aesthetic

Subtle touches of fun or personality are welcome

Layout must work well when overlaid by Facebook UI elements (like profile photo & call-to-action buttons)

Who I Am:
I'm a well-known residential real estate agent in the Redlands area, known for high-energy campaigns, premium video marketing, and a results-driven approach. My brand is fun, fresh, and high-performing — just like the real estate campaigns I run.

Files to be Provided (after selection):

Ridgeway Moss logo in high-res

Brand colour palette / style reference

Optional photo references if local imagery is not sourced by designer

Final Notes:

Make sure all text is legible on mobile and desktop

Original, layered design files must be delivered (PSD or AI preferred)

Bonus points if it feels uniquely “Bayside Queensland” while maintaining a national-level professional polish

Target Market(s)

Alexandra Hills, Capalaba & Sheldon

Industry/Entity Type

Real Estate

Colors
0054AA
0677BA
7BADD7
CADEEF
E8F1F8

Requirements
Must have
• Headshot, Mobile Number 0491 726 805, Suburbs - Alexandra Hills, Capalaba & Sheldon
Nice to have
• White, Crisp & Professional. Bottom Banner with Suburb List. Specialising in Alexandra Hills, Capalaba & Sheldon

```html
<!DOCTYPE html>
<html lang="en">
<head>
<meta charset="utf-8">
<title>Ridgeway Moss – Facebook Cover &amp; Profile Icon</title>
<link href="https://fonts.googleapis.com/css2?family=Montserrat:wght@300;500;700&family=Oswald:wght@500;600&display=swap" rel="stylesheet">
<style>
  :root{
    --navy:#1f2566;
    --navy-deep:#181d55;
    --glow:#c9d2ee;
    --tan:#d8a66b;
    --white:#ffffff;
    --stage:#eef1f6;
    --suit:#3a4a66;
    --suit-light:#6b7a93;
  }
  *{margin:0;padding:0;box-sizing:border-box}
  html,body{width:1200px;height:881px;overflow:hidden;background:var(--stage)}
  .canvas{position:relative;width:1200px;height:881px}

  /* Cover */
  .cover{position:absolute;left:0;top:0;width:1200px;height:457px;overflow:hidden;
    background:radial-gradient(circle at 948px 170px,var(--glow) 0,#6d78b6 70px,var(--navy) 210px,var(--navy-deep) 100%);}
  .brand-name{position:absolute;left:456px;top:88px;transform:translateX(-50%);
    font-family:"Montserrat",sans-serif;font-weight:300;font-size:52px;letter-spacing:3px;
    color:var(--white);white-space:nowrap;text-transform:uppercase;line-height:1;z-index:2}
  .tagline{position:absolute;left:133px;top:185px;width:648px;height:55px;background:var(--white);
    border-radius:12px;box-shadow:0 6px 0 rgba(0,0,0,.18);display:flex;align-items:center;justify-content:center;
    font-family:"Oswald",sans-serif;font-weight:600;font-size:24px;color:var(--navy);letter-spacing:0;white-space:nowrap;z-index:2}
  .suburbs{position:absolute;left:288px;top:268px;list-style:none}
  .suburbs li{display:flex;align-items:center;height:44px;
    font-family:"Oswald",sans-serif;font-weight:500;font-size:27px;color:var(--tan);letter-spacing:.5px}
  .suburbs svg{width:30px;height:30px;margin-right:22px}
  .call{position:absolute;left:148px;top:362px;display:flex;align-items:center;white-space:nowrap}
  .call-label{font-family:"Montserrat",sans-serif;font-weight:700;font-size:29px;color:var(--white)}
  .call svg{width:44px;height:44px;margin:0 22px 0 44px}
  .call-number{font-family:"Montserrat",sans-serif;font-weight:700;font-size:37px;color:var(--white);letter-spacing:.5px}
  .agent-photo{position:absolute;left:800px;top:44px;width:270px;height:413px;
    border-radius:135px 135px 0 0;
    background:linear-gradient(180deg,#8a93b8 0%,var(--suit-light) 35%,var(--suit) 100%)}

  /* Profile icon */
  .profile{position:absolute;left:440px;top:520px;width:320px;height:320px;border-radius:50%;overflow:hidden;
    border:6px solid var(--white);box-shadow:0 4px 14px rgba(0,0,0,.15);
    background:radial-gradient(circle at 50% 60%,#6d78b6 0,var(--navy) 120px,var(--navy-deep) 100%)}
  .profile-name{position:absolute;top:46px;left:0;width:100%;text-align:center;
    font-family:"Montserrat",sans-serif;font-weight:300;font-size:20px;letter-spacing:2px;color:var(--white);text-transform:uppercase}
  .profile-photo{position:absolute;left:78px;top:92px;width:152px;height:230px;border-radius:76px 76px 0 0;
    background:linear-gradient(180deg,#8a93b8 0%,var(--suit-light) 40%,var(--suit) 100%)}
</style>
</head>
<body>
<main class="canvas">
  <section class="cover">
    <div class="agent-photo" role="img" aria-label="Headshot of the agent in a blue suit jacket and white shirt"></div>
    <div class="brand-name">Ridgeway Moss</div>
    <div class="tagline">SELLING FASTER. SELLING SMARTER. SELLING RIDGEWAY</div>
    <ul class="suburbs">
      <li><svg viewBox="0 0 30 30"><circle cx="15" cy="15" r="15" fill="#fff"/><path d="M8.5 15.5l4.2 4.2 8.8-9" fill="none" stroke="#1f2566" stroke-width="3" stroke-linecap="round" stroke-linejoin="round"/></svg>ALEXANDRA HILLS</li>
      <li><svg viewBox="0 0 30 30"><circle cx="15" cy="15" r="15" fill="#fff"/><path d="M8.5 15.5l4.2 4.2 8.8-9" fill="none" stroke="#1f2566" stroke-width="3" stroke-linecap="round" stroke-linejoin="round"/></svg>CAPALABA &amp; SHELDON</li>
    </ul>
    <div class="call">
      <span class="call-label">Call Now</span>
      <svg viewBox="0 0 44 44"><circle cx="22" cy="22" r="22" fill="#d8a66b"/><path d="M16 12.5c1-.6 2-.3 2.6.6l2 3.2c.5.9.3 1.9-.5 2.5l-1.4 1c.9 2.2 2.6 4 4.8 5l1.1-1.4c.6-.8 1.7-1 2.5-.4l3.1 2.1c.9.6 1.1 1.7.5 2.6l-1.2 1.8c-.8 1.2-2.3 1.6-3.6 1.1-5.4-2.1-9.6-6.4-11.5-11.8-.4-1.3 0-2.7 1.1-3.5z" fill="#fff"/></svg>
      <span class="call-number">0491 726 805</span>
    </div>
  </section>

  <section class="profile">
    <div class="profile-name">Ridgeway Moss</div>
    <div class="profile-photo" role="img" aria-label="Headshot of the agent for the profile icon"></div>
  </section>
</main>
</body>
</html>
```